Develop new wine label for entry level Greek wines **

We need a label design for the new line of entry level Greek wines.

We will have 4 SKU: red dry wine, red semi sweet wine, white dry wine, white semi-sweet wines.

We would like to see traditional greek houses on it.

There needs to be a slight colour difference between dry and semi sweet wines (you can maybe change colours of some details in order to differentiate wines on the shelf).

We would like to use designs that use white and blue colours (I attached some images for your inspiration). The glass bottle will be transparent so keep in mind how the label will coordinate with the colour of the wine itself.

The label needs to communicate that the wine is from Greece, this wine is simple, approachable, easy to drink, modern and fun.

The brand name is the ancient Greek word "kelvo". Quoting knowlark: " Kelvo (ancient Greek: κἐλβος, plural: κἐλβοι; English prefix: eco- for ecology and economics) refers to three related but distinct concepts: the family, the family's property, and the house.".

So feel free to further elaborate on the concept.

The text that should appear on the label:
1. Brand name - Kelvo (a good idea would be to use a greek style shrift would be great to mimic greek letters κέλβος).
2. White semi-sweet / White dry / Red semi-sweet / Red dry

Target Market(s)

Ukraine

Font styles to use
Serif

Colors
33a6d7
cee9f5
ffffff
e34297

Requirements
Must have
• The customer needs to look at the bottle and understand that is it from Greece straight away.

```html
<!DOCTYPE html>
<html lang="en">
<head>
<meta charset="utf-8">
<title>Kelvo — White Dry Wine Label</title>
<link rel="stylesheet" href="https://fonts.googleapis.com/css2?family=Gentium+Book+Plus&family=Cinzel&family=Libre+Baskerville&display=swap">
<style>
  :root {
    --paper: #ffffff;
    --ink: #111111;
    --border-tone: #6b6b6b;
    --sky: #4f86a8;
    --sky-light: #9fc2d6;
    --dome: #1f4f78;
    --wall: #eef2f5;
  }
  * { margin: 0; padding: 0; box-sizing: border-box; }
  html, body {
    width: 1200px;
    height: 1200px;
    overflow: hidden;
    background: var(--paper);
  }
  .canvas {
    position: relative;
    width: 1200px;
    height: 1200px;
    background: var(--paper);
  }
  .wine-label {
    position: absolute;
    left: 355px;
    top: 242px;
    width: 490px;
    height: 716px;
  }
  .label-frame {
    position: absolute;
    inset: 0;
    width: 490px;
    height: 716px;
  }
  .brand-name {
    position: absolute;
    top: 170px;
    left: 0;
    width: 100%;
    text-align: center;
    font-family: "Gentium Book Plus", serif;
    font-size: 86px;
    line-height: 1;
    color: var(--ink);
  }
  .village-scene {
    position: absolute;
    left: 92px;
    top: 312px;
    width: 300px;
    height: 215px;
    border-radius: 46% / 40%;
    background:
      radial-gradient(ellipse 34% 30% at 55% 78%, var(--dome) 0%, rgba(31,79,120,0.6) 55%, rgba(31,79,120,0) 100%),
      radial-gradient(ellipse 60% 40% at 50% 85%, var(--wall) 0%, rgba(238,242,245,0) 100%),
      linear-gradient(180deg, var(--sky) 0%, var(--sky-light) 45%, var(--wall) 75%, var(--wall) 100%);
    -webkit-mask-image: radial-gradient(ellipse 50% 50% at 50% 50%, #000 70%, transparent 100%);
    mask-image: radial-gradient(ellipse 50% 50% at 50% 50%, #000 70%, transparent 100%);
  }
  .wine-type {
    position: absolute;
    top: 566px;
    left: 0;
    width: 100%;
    text-align: center;
    font-family: "Cinzel", serif;
    font-size: 35px;
    letter-spacing: 0.5px;
    color: var(--ink);
  }
  .vintage {
    position: absolute;
    top: 622px;
    left: 0;
    width: 100%;
    text-align: center;
    font-family: "Libre Baskerville", serif;
    font-size: 31px;
    color: var(--ink);
  }
</style>
</head>
<body>
  <main class="canvas">
    <section class="wine-label">
      <svg class="label-frame" viewBox="0 0 490 716" xmlns="http://www.w3.org/2000/svg">
        <path d="M3,230 C3,102 112,3 245,3 C378,3 487,102 487,230 L487,654 Q487,713 428,713 L62,713 Q3,713 3,654 Z"
              fill="none" stroke="var(--ink)" stroke-width="3"/>
        <path role="img" aria-label="Greek key meander border band"
              fill="var(--border-tone)" fill-rule="evenodd"
              d="M10,232 C10,108 116,10 245,10 C374,10 480,108 480,232 L480,650 Q480,706 424,706 L66,706 Q10,706 10,650 Z
                 M40,238 C40,126 136,40 245,40 C354,40 450,126 450,238 L450,640 Q450,676 414,676 L76,676 Q40,676 40,640 Z"/>
        <path d="M46,240 C46,131 139,46 245,46 C351,46 444,131 444,240 L444,638 Q444,670 412,670 L78,670 Q46,670 46,638 Z"
              fill="none" stroke="var(--ink)" stroke-width="3"/>
      </svg>
      <h1 class="brand-name" lang="grc">κἐλβος</h1>
      <div class="village-scene" role="img" aria-label="Whitewashed Greek village with blue domes under a cloudy sky"></div>
      <p class="wine-type">WHITE DRY WINE</p>
      <p class="vintage">2021</p>
    </section>
  </main>
</body>
</html>
```